Making 6 Posters and 2 large posters for coffee shop

We are Maple Bean Depot (similar to a brewhollow), planning to make 3 boards for menu, 3 photos to be printed onto the board, and 2 large posters. (dimensions provided). We believe this is a very simple project with not much additional work required as all pictures have been provided.
We are asking for minimalist design. Very simple. All photos have been provided. 3 of the boards, and 2 for the large posters. The menu has been done but it is in PDF and require recreation (pls make similar design)
The menu board and the 3 other photos are roughly square shape. While dimensions are not provided by our contractors yet, designers can roughly get the dimension from the photos of the boards we are planning to replace.
All these posters will be printed with no frames. So it will look something like those menu board at brewhollow.
Urgently need it in next 24 hours.
Instructions all in PPT attached.
File Link provided:
http://8qlnk.io/3kR7tWz
Thanks.
---- Edited
For the pictures, we are looking for borders like this if possible (VORA - expensive looking border but platinum white, and dark background.) for the large poster, we liek black themed background with some glow if possible around the cups like the telvix logo)
http://www.mockvault-demo.com/images/thumbs/Dark-Pass-psd48213.png
http://www.techtrove-news.com/wp-content/uploads/2013/11/telvix-signage.jpg
Target Market(s)
Professionals - Lawyers, Bankers, Brokers
Industry/Entity Type
Coffee Shop

```html
<!DOCTYPE html>
<html lang="en">
<head>
<meta charset="UTF-8">
<title>Maple Bean Depot – Menu Boards</title>
<link href="https://fonts.googleapis.com/css2?family=Alfa+Slab+One&family=Oswald:wght@400;600&family=Roboto+Condensed:wght@400;700&display=swap" rel="stylesheet">
<style>
  :root {
    --backdrop: #ecebe8;
    --board: #0b0b0b;
    --board-edge: #1a1a1a;
    --platinum: #d9d9d6;
    --text: #e8e8e8;
    --muted: #a9a9a9;
    --rule: #4a4a4a;
    --row-rule: #262626;
    --cup-yellow: #e3c21a;
    --photo-dark: #2a2418;
    --photo-warm: #8a7428;
  }
  * { box-sizing: border-box; margin: 0; padding: 0; }
  html, body { width: 1200px; height: 900px; overflow: hidden; }
  body {
    background: var(--backdrop);
    font-family: "Roboto Condensed", "Arial Narrow", sans-serif;
    display: flex;
    align-items: center;
    justify-content: center;
  }
  .board-row {
    display: flex;
    gap: 12px;
  }
  .board {
    position: relative;
    width: 380px;
    height: 390px;
    background: var(--board);
    border: 2px solid var(--board-edge);
  }

  /* Photo boards */
  .photo-board::before {
    content: "";
    position: absolute;
    inset: 10px;
    border: 2px solid var(--platinum);
    pointer-events: none;
  }
  .brand {
    position: absolute;
    top: 28px;
    left: 30px;
    display: flex;
    align-items: flex-end;
    gap: 8px;
  }
  .brand-dot {
    width: 30px;
    height: 30px;
    border-radius: 50%;
    background: var(--cup-yellow);
  }
  .brand-name {
    font-family: "Oswald", sans-serif;
    font-weight: 600;
    font-size: 10px;
    letter-spacing: 0.3px;
    color: var(--text);
    text-transform: uppercase;
    white-space: nowrap;
    margin-bottom: -6px;
  }
  .photo {
    position: absolute;
    background: linear-gradient(135deg, var(--photo-dark) 0%, var(--photo-warm) 100%);
  }
  .photo-coffee {
    left: 20px;
    top: 135px;
    width: 280px;
    height: 160px;
  }
  .photo-sandwich {
    left: 62px;
    top: 150px;
    width: 268px;
    height: 160px;
  }

  /* Menu board */
  .menu-board {
    padding: 12px 22px 14px;
    color: var(--text);
  }
  .edge-band {
    height: 5px;
    border-top: 1px dotted var(--muted);
    border-bottom: 1px dotted var(--muted);
  }
  .menu-title {
    display: flex;
    align-items: center;
    gap: 8px;
    margin: 8px 0 6px;
  }
  .menu-title .line {
    flex: 1;
    height: 5px;
    border-top: 1px solid var(--muted);
    border-bottom: 1px solid var(--muted);
  }
  .menu-title h1 {
    font-family: "Alfa Slab One", serif;
    font-weight: 400;
    font-size: 17px;
    letter-spacing: 1px;
    color: var(--text);
  }
  .menu {
    font-size: 7px;
    line-height: 1;
    padding: 0 22px;
  }
  .col-head, .item {
    display: grid;
    grid-template-columns: 1fr 22px 22px 22px;
    align-items: center;
  }
  .col-head {
    font-size: 5px;
    color: var(--muted);
    height: 9px;
  }
  .col-head span, .item span:not(:first-child) { text-align: center; }
  .item span { white-space: nowrap; }
  .section-title {
    font-size: 9px;
    color: var(--text);
    padding: 3px 0 2px;
    border-bottom: 1px solid var(--rule);
  }
  .section + .section { margin-top: 7px; }
  .item {
    height: 9px;
    border-bottom: 1px solid var(--row-rule);
    color: var(--text);
  }
  .item.sub {
    font-size: 5px;
    color: var(--muted);
    height: 7px;
  }
  .item .span-all {
    grid-column: 2 / 5;
    text-align: right !important;
  }
  .tea-list {
    display: grid;
    grid-template-columns: 1fr 1fr;
    font-size: 5px;
    color: var(--muted);
    row-gap: 2px;
    padding-top: 3px;
  }
  .tea-list span { white-space: nowrap; }
  .menu-foot {
    position: absolute;
    left: 22px;
    right: 22px;
    bottom: 14px;
  }
  .menu-foot .rule {
    height: 1px;
    background: var(--rule);
    margin-bottom: 4px;
  }
</style>
</head>
<body>
  <main class="board-row">
    <section class="board photo-board">
      <div class="brand">
        <span class="brand-dot"></span>
        <span class="brand-name">Maple Bean Depot</span>
      </div>
      <div class="photo photo-coffee" role="img" aria-label="Photo: latte art in a yellow cup and saucer beside scattered coffee beans"></div>
    </section>

    <section class="board menu-board">
      <div class="edge-band"></div>
      <div class="menu-title">
        <span class="line"></span>
        <h1>HOT BEVERAGE</h1>
        <span class="line"></span>
      </div>
      <div class="menu">
        <div class="section">
          <div class="col-head"><span></span><span>Small</span><span>Medium</span><span>Large</span></div>
          <div class="section-title">Hot Coffee</div>
          <div class="item"><span>Latte / Flat White</span><span>5</span><span>5.5</span><span>6</span></div>
          <div class="item"><span>Caramel Latte</span><span>5.8</span><span>6.3</span><span>6.8</span></div>
          <div class="item"><span>Hazelnut Latte</span><span>5.8</span><span>6.3</span><span>6.8</span></div>
          <div class="item"><span>Specialty Latte</span><span>5.8</span><span>6.3</span><span>6.8</span></div>
          <div class="item sub"><span>Vanilla, Caramel or Honey</span><span></span><span></span><span></span></div>
          <div class="item"><span>Mocha / White Mocha</span><span>5.8</span><span>6.3</span><span>6.8</span></div>
          <div class="item"><span>Cappuccino</span><span>5</span><span>5.5</span><span>6</span></div>
          <div class="item"><span>Americano</span><span>4.5</span><span>5</span><span>5.5</span></div>
          <div class="item"><span>Macchiato</span><span>4.5</span><span></span><span></span></div>
          <div class="item"><span>Espresso</span><span>4</span><span></span><span></span></div>
          <div class="item"><span>Extra Shot</span><span>1</span><span></span><span></span></div>
        </div>
        <div class="section">
          <div class="section-title">Hot Matcha</div>
          <div class="item"><span>Matcha Latte</span><span>6</span><span>6.5</span><span>7</span></div>
        </div>
        <div class="section">
          <div class="section-title">Hot Chocolate</div>
          <div class="item"><span>Rich Chocolate</span><span>5.5</span><span>6</span><span>6.5</span></div>
        </div>
        <div class="section">
          <div class="section-title">Hot Brewed Tea</div>
          <div class="item"><span>Chai Latte</span><span>5.5</span><span>6</span><span>6.5</span></div>
          <div class="item sub"><span>Spiced black tea with steamed milk</span><span></span><span></span><span></span></div>
          <div class="item"><span>Earl Grey Latte</span><span>5.5</span><span>6</span><span>6.5</span></div>
          <div class="item"><span>Peppermint Tea</span><span>4.5</span><span>5</span><span>5.5</span></div>
          <div class="item"><span>Tea Pot Selection</span><span class="span-all">Single Pot</span></div>
          <div class="tea-list">
            <span>English Breakfast Tea</span><span>Green Jasmine Tea</span>
            <span>Chamomile Tea</span><span>Lemon Ginger Tea</span>
            <span>Darjeeling Tea</span><span>Wild Berry Tea</span>
          </div>
        </div>
      </div>
      <div class="menu-foot">
        <div class="rule"></div>
        <div class="edge-band"></div>
      </div>
    </section>

    <section class="board photo-board">
      <div class="brand">
        <span class="brand-dot"></span>
        <span class="brand-name">Maple Bean Depot</span>
      </div>
      <div class="photo photo-sandwich" role="img" aria-label="Photo: croissant sandwich with salmon and salad leaves on a yellow plate"></div>
    </section>
  </main>
</body>
</html>
```